Visitenkarten-Design für Handel mit Handstrickgarnen
Zielgruppe
Handel mit Handstrickgarnen, besonders Farbverläufe und handgefärbte Garne, aber auch Design von Strickmode. Die Zielgruppe sind alle, die gerne stricken oder häkeln, insbesondere Frauen aller Altersgruppen.
Aufgabenstellung
Schöne Farbverläufe bzw. Farbharmonien sind mir besonders wichtig und sollten insgesamt ins Auge stechen ohne jedoch zu grell bunt zu wirken. Sanft ineinander fließende Farben wären ideal, gerne auch etwas kräftigere Farben. Das Motiv des Logos könnte auch im Negativ sein auf dunklerem Hintergrund.

```html
<!DOCTYPE html>
<html lang="de">
<head>
<meta charset="utf-8">
<title>Fadenreich – Visitenkarte</title>
<link href="https://fonts.googleapis.com/css2?family=Questrial&family=Allura&display=swap" rel="stylesheet">
<style>
  :root{
    --bg:#ecebe8;
    --card:#ffffff;
    --blue:#7b96c8;
    --blue-deep:#6681b8;
    --blue-soft:#a9bde0;
    --ink:#1c1c1c;
    --rule:#9a9a9a;
  }
  *{box-sizing:border-box;margin:0;padding:0}
  html,body{width:1200px;height:857px;overflow:hidden;background:var(--bg)}
  body{font-family:"Questrial",sans-serif;color:var(--ink);position:relative}

  .card{position:absolute;width:540px;height:340px;border-radius:4px;
        box-shadow:0 6px 20px rgba(0,0,0,.18);overflow:hidden}

  /* Rückseite */
  .card--back{left:45px;top:258px;
    background:radial-gradient(ellipse at 45% 40%,var(--blue-soft) 0%,var(--blue-deep) 70%)}
  .back-name{position:absolute;left:0;right:0;top:146px;text-align:center;
    font-size:44px;letter-spacing:2px;color:rgba(255,255,255,.55)}

  /* Vorderseite */
  .card--front{left:615px;top:258px;background:var(--card)}
  .side-band{position:absolute;left:0;top:0;bottom:0;width:72px;background:var(--blue)}
  .side-square{position:absolute;left:12px;bottom:14px;width:48px;height:48px;background:var(--card)}

  .brand{position:absolute;left:72px;right:0;top:48px;display:flex;
    justify-content:center;align-items:center;gap:12px}
  .brand-dot{width:18px;height:18px;border-radius:50%;background:var(--blue-deep)}
  .brand-name{font-size:34px;color:var(--blue-deep)}

  .person{position:absolute;left:72px;right:0;top:122px;text-align:center}
  .person-name{font-family:"Allura",cursive;font-size:52px;line-height:1}
  .person-role{font-size:14px;margin-top:4px}

  .contact{position:absolute;left:130px;top:210px;display:grid;
    grid-template-columns:90px 1fr;row-gap:2px;font-size:19px;line-height:24px}
  .contact dd{text-align:right;padding-left:20px}
  .rule{position:absolute;left:220px;right:90px;top:286px;border-top:1px solid var(--rule)}
  .footer{position:absolute;left:130px;top:298px;font-size:15px}
</style>
</head>
<body>
  <section class="card card--back" aria-label="Rückseite der Visitenkarte">
    <div class="back-name">Fadenreich</div>
  </section>

  <section class="card card--front" aria-label="Vorderseite der Visitenkarte">
    <div class="side-band"><div class="side-square"></div></div>

    <div class="brand">
      <span class="brand-dot"></span>
      <span class="brand-name">Fadenreich</span>
    </div>

    <div class="person">
      <div class="person-name">Vorname Name</div>
      <div class="person-role">Position | Berufsbezeichnung</div>
    </div>

    <dl class="contact">
      <dt>E-Mail:</dt><dd>info@Firmenname.de</dd>
      <dt>Mobil:</dt><dd>+49 157 777 77 77</dd>
      <dt>Büro:</dt><dd>+49 30 777 77 77</dd>
    </dl>
    <div class="rule"></div>
    <div class="footer">www.Firmenname.de | Adresse | PLZ | Ort</div>
  </section>
</body>
</html>
```